qoCover Business Card Design Project

We need a business card design for qoCover. qoCover is an underwriting agency. Underwriting agencies act on behalf of insurers, to underwrite insurance. We will be operating in specialised classes of insurance initially and looking to expand from there. We would like to see designs that incorporate our logo colours as well as a contrasting stand out colour - also we'd like the logo itself to be embossed on the card.

Industry/Entity Type

Insurance

Requirements
Must have
• Logo on front
Nice to have
• Logo solely featured on back of card
Should not have
• Please do not use comic cans font :)

```html
<!DOCTYPE html>
<html lang="en">
<head>
<meta charset="utf-8">
<title>qoCover Business Card</title>
<link href="https://fonts.googleapis.com/css2?family=Arimo:wght@400;700&display=swap" rel="stylesheet">
<style>
  :root {
    --stage: #e9e7e4;
    --card: #ffffff;
    --brand-blue: #1f5fae;
    --ink: #2b2e33;
    --charcoal: #3b3f45;
    --muted: #55595f;
  }
  * { margin: 0; padding: 0; box-sizing: border-box; }
  html, body { width: 1200px; height: 900px; overflow: hidden; }
  body {
    background: var(--stage);
    font-family: "Arimo", Arial, sans-serif;
    position: relative;
  }
  .card {
    position: absolute;
    top: 326px;
    width: 540px;
    height: 308px;
    background: var(--card);
    border-radius: 14px;
    overflow: hidden;
    box-shadow: 0 2px 6px rgba(0,0,0,0.18);
  }
  .card--front { left: 40px; }
  .card--back { left: 623px; }

  .brand-name {
    color: var(--brand-blue);
    font-weight: 700;
    letter-spacing: -0.5px;
  }
  .card--front .brand-name {
    position: absolute;
    left: 36px;
    top: 30px;
    font-size: 42px;
  }
  .holder {
    position: absolute;
    left: 38px;
    top: 118px;
  }
  .holder__name {
    color: var(--brand-blue);
    font-weight: 700;
    font-size: 23px;
    line-height: 1.1;
  }
  .holder__role {
    color: var(--ink);
    font-size: 16px;
    margin-top: 2px;
  }
  .contacts {
    position: absolute;
    left: 38px;
    top: 200px;
    list-style: none;
  }
  .contacts li {
    display: flex;
    align-items: center;
    gap: 6px;
    height: 23px;
    font-size: 17px;
    color: var(--ink);
  }
  .contacts svg { width: 16px; height: 16px; fill: var(--ink); flex: none; }
  .front-band {
    position: absolute;
    left: 0;
    bottom: 0;
    width: 540px;
    height: 40px;
  }

  .back-mark {
    position: absolute;
    left: 0;
    right: 0;
    top: 120px;
    display: flex;
    align-items: center;
    justify-content: center;
    gap: 14px;
  }
  .back-mark__dot {
    width: 40px;
    height: 40px;
    border-radius: 50%;
    background: var(--brand-blue);
  }
  .card--back .brand-name { font-size: 48px; }
  .web {
    position: absolute;
    left: 0;
    right: 0;
    top: 268px;
    text-align: center;
    font-size: 15px;
    color: var(--muted);
  }
</style>
</head>
<body>
  <section class="card card--front">
    <div class="brand-name">qoCover</div>
    <div class="holder">
      <div class="holder__name">Liam Porter</div>
      <div class="holder__role">IT Manager</div>
    </div>
    <ul class="contacts">
      <li>
        <svg viewBox="0 0 16 16" aria-hidden="true"><path d="M2 5c0-2 2-3 6-3s6 1 6 3v1h-3V5H5v1H2zM4 7h8l2 6H2z"/></svg>
        <span>: 400-5550-2718</span>
      </li>
      <li>
        <svg viewBox="0 0 16 16" aria-hidden="true"><path d="M5 1h6a1 1 0 0 1 1 1v12a1 1 0 0 1-1 1H5a1 1 0 0 1-1-1V2a1 1 0 0 1 1-1zm1 2v7h4V3z"/></svg>
        <span>: 400-5550-9031</span>
      </li>
      <li>
        <svg viewBox="0 0 16 16" aria-hidden="true"><path d="M1 3h14v10H1zm1.5 1.5v.4L8 9l5.5-4.1v-.4zm0 2.3v4.7h11V6.8L8 10.9z"/></svg>
        <span>: liam@qocover.com.au</span>
      </li>
    </ul>
    <svg class="front-band" viewBox="0 0 540 40" aria-hidden="true">
      <path d="M0 14 H400 C420 14 428 28 445 40 H0 Z" fill="var(--charcoal)"/>
    </svg>
  </section>

  <section class="card card--back">
    <div class="back-mark">
      <span class="back-mark__dot"></span>
      <span class="brand-name">qoCover</span>
    </div>
    <div class="web">www.qocover.com.au</div>
  </section>
</body>
</html>
```